" Busco uma arte para capa de um livro que estou concluindo. Título do livro: "Entre marés e faróis. Um diário de viagens pelo litoral esquecido". "

```html
<!DOCTYPE html>
<html lang="pt">
<head>
<meta charset="utf-8">
<title>Entre marés e faróis — capa</title>
<link rel="stylesheet" href="https://fonts.googleapis.com/css2?family=Cinzel:wght@500&family=Playfair+Display:wght@500&family=Cormorant+Garamond:wght@500&display=swap">
<style>
  :root {
    --page-bg: #ececec;
    --cover-ink: #17161f;
    --cover-ink-deep: #0d0c14;
    --title-cream: #efe6d2;
    --subtitle-cream: #ddd3bd;
    --art-navy: #1c2340;
    --art-teal: #2f7f9a;
    --art-sky: #8fd0e0;
    --art-amber: #d98a3e;
    --art-rust: #8a3d22;
    --art-gold: #f0c074;
  }
  * { margin: 0; padding: 0; box-sizing: border-box; }
  html, body {
    width: 1200px;
    height: 1200px;
    overflow: hidden;
    background: var(--page-bg);
  }
  .canvas {
    width: 1200px;
    height: 1200px;
    display: flex;
    align-items: center;
    justify-content: center;
  }
  .book-cover {
    position: relative;
    width: 760px;
    height: 1080px;
    background: linear-gradient(180deg, var(--cover-ink) 0%, var(--cover-ink-deep) 100%);
    box-shadow: 0 20px 50px rgba(0,0,0,0.25);
    overflow: hidden;
  }
  .cover-author {
    position: absolute;
    top: 62px;
    left: 0;
    right: 0;
    text-align: center;
    font-family: "Cinzel", serif;
    font-weight: 500;
    font-size: 26px;
    letter-spacing: 2px;
    color: var(--subtitle-cream);
  }
  .cover-title {
    position: absolute;
    top: 118px;
    left: 0;
    right: 0;
    text-align: center;
    font-family: "Playfair Display", serif;
    font-weight: 500;
    font-size: 84px;
    line-height: 1.0;
    color: var(--title-cream);
    letter-spacing: -1px;
  }
  .cover-subtitle {
    position: absolute;
    top: 306px;
    left: 0;
    right: 0;
    text-align: center;
    font-family: "Cormorant Garamond", serif;
    font-weight: 500;
    font-size: 36px;
    line-height: 1.12;
    color: var(--subtitle-cream);
  }
  .cover-artwork {
    position: absolute;
    left: 0;
    right: 0;
    top: 420px;
    bottom: 0;
    background:
      radial-gradient(ellipse 40% 30% at 50% 48%, var(--art-sky) 0%, rgba(143,208,224,0) 70%),
      radial-gradient(ellipse 70% 40% at 50% 92%, var(--art-gold) 0%, rgba(240,192,116,0) 70%),
      radial-gradient(ellipse 35% 35% at 20% 55%, var(--art-amber) 0%, rgba(217,138,62,0) 75%),
      radial-gradient(ellipse 35% 35% at 82% 55%, var(--art-rust) 0%, rgba(138,61,34,0) 75%),
      radial-gradient(ellipse 50% 40% at 55% 40%, var(--art-teal) 0%, rgba(47,127,154,0) 75%),
      linear-gradient(180deg, var(--cover-ink-deep) 0%, var(--art-navy) 30%, #3a2a30 70%, var(--art-rust) 100%);
  }
</style>
</head>
<body>
  <main class="canvas">
    <article class="book-cover">
      <p class="cover-author">Helena Moura Castro</p>
      <h1 class="cover-title">Entre marés<br>e faróis</h1>
      <p class="cover-subtitle">Um diário de viagens<br>pelo litoral esquecido</p>
      <div class="cover-artwork" role="img" aria-label="Ilustração em camadas de papel: montanhas coloridas, céu noturno estrelado e um livro aberto dourado na base"></div>
    </article>
  </main>
</body>
</html>
```